Cleaners Needs Bounce-Back Coupon For Laundry Service

We need a "bounce-back" coupon to attach to peoples dry cleaning orders that offers one free wash-n-fold laundry service. Right now we always attach their receipt to the bag that contains their dry cleaning when we return it. We'd like to also attach a coupon that will entice them to come try our laundry service.

Background on the service: We sort, wash, dry, and fold the laundry for customers and then neatly put it in a nice bag that makes returning very convenient. Their laundry comes out fresh, clean, smelling great, and without the hassle of doing it themselves. We have a great return rate. Most customers that try out the service become long term customers. The goal is to get our dry cleaning customers to come try it out.

Requirements:
* 5" x 8" and one-sided.
* To be printed on a standard color of card stock.
* Must incorporate our logo.
* Needs a place for us to fill in an expiration date. We'll fill in a date about two weeks out from the time they pick up their dry cleaning.
* Limit one coupon per customer.
* Limit 50 pounds of laundry per coupon.

```html
<!DOCTYPE html>
<html lang="en">
<head>
<meta charset="utf-8">
<title>Suds on Fifth – Free Wash-n-Fold Coupon</title>
<link rel="stylesheet" href="https://fonts.googleapis.com/css2?family=Open+Sans:wght@400;600;700&family=Roboto+Condensed:wght@700;800&display=swap">
<style>
  :root {
    --page: #ececec;
    --card-top: #ffffff;
    --card-mist: #e6e8ea;
    --card-sky: #cfe6f2;
    --brand-blue: #2f4fb8;
    --brand-blue-light: #6f8fe6;
    --brand-orange: #f0662a;
    --brand-orange-dark: #d9531b;
    --offer-red: #e8202a;
    --ink: #1c1c1c;
    --white: #ffffff;
    --basket: #6b4a36;
    --towel: #a9a594;
  }
  * { box-sizing: border-box; margin: 0; padding: 0; }
  html, body { width: 952px; height: 1200px; overflow: hidden; }
  body { background: var(--page); font-family: "Open Sans", Arial, sans-serif; color: var(--ink); position: relative; }

  .coupon {
    position: absolute; left: 126px; top: 40px; width: 700px; height: 1120px;
    overflow: hidden;
    background:
      radial-gradient(ellipse 360px 520px at 640px 760px, var(--card-sky) 0%, rgba(207,230,242,0) 70%),
      linear-gradient(180deg, var(--card-top) 0%, var(--card-mist) 40%, var(--card-mist) 100%);
  }

  .hero-photo {
    position: absolute; left: 0; top: 0; width: 700px; height: 342px;
    background: linear-gradient(120deg, #f4f4f4 0%, #dfe9ea 35%, #c9dcdf 55%, #f1ece4 75%, #e9b96a 100%);
  }

  .washer-illustration {
    position: absolute; left: 27px; top: 241px; width: 187px; height: 237px;
    border-radius: 14px;
    background: linear-gradient(160deg, #5c7fe0 0%, #2c4db3 70%, #1f3790 100%);
  }

  .logo {
    position: absolute; left: 214px; top: 290px; width: 455px; height: 120px;
    display: flex; align-items: center; gap: 18px; padding-left: 26px;
    background: linear-gradient(180deg, #a9c6f0 0%, #7ea6e6 100%);
    border-radius: 0 30px 0 0;
  }
  .logo-mark { width: 28px; height: 28px; background: var(--brand-orange); flex: none; }
  .logo-name {
    font-family: "Open Sans", Arial, sans-serif; font-weight: 600;
    font-size: 64px; line-height: 1; color: var(--white);
  }

  .headline {
    position: absolute; left: 0; top: 482px; width: 700px; text-align: center;
    font-family: "Roboto Condensed", "Arial Narrow", sans-serif; font-weight: 800;
    font-size: 36px; letter-spacing: -0.3px; color: var(--brand-blue-light);
    -webkit-text-stroke: 1.4px var(--brand-blue);
  }

  .offer-bubble { position: absolute; left: 105px; top: 544px; width: 500px; height: 330px; }
  .care-icons { position: absolute; left: 236px; top: 573px; width: 220px; height: 36px; }

  .offer-amount {
    position: absolute; left: 128px; top: 632px; width: 180px; text-align: center;
    color: var(--offer-red); font-weight: 700;
  }
  .offer-amount .number { display: block; font-size: 120px; line-height: 0.95; letter-spacing: -4px; }
  .offer-amount .unit { display: block; font-size: 30px; line-height: 1.1; }

  .offer-terms {
    position: absolute; left: 334px; top: 634px;
    color: var(--white); font-weight: 700; font-size: 42px; line-height: 1.3;
  }

  .limit-note { position: absolute; left: 352px; top: 830px; width: 330px; text-align: center; font-size: 24px; }

  .expiry-field {
    position: absolute; left: 356px; top: 869px; width: 315px; height: 64px;
    background: var(--white); border: 1px solid #c8c8c8;
    box-shadow: 4px 5px 6px rgba(0,0,0,0.35);
  }
  .expiry-label { position: absolute; left: 356px; top: 942px; width: 315px; text-align: center; font-size: 21px; }

  .contact { position: absolute; right: 32px; top: 1008px; text-align: right; }
  .contact .phone { display: flex; justify-content: flex-end; align-items: center; gap: 8px; font-size: 32px; font-weight: 700; }
  .contact .phone svg { width: 34px; height: 34px; }
  .contact .address { font-size: 23px; margin-top: 4px; }

  .basket-photo {
    position: absolute; left: 0; top: 940px; width: 334px; height: 180px;
    background: linear-gradient(180deg, var(--towel) 0%, #8c7a66 30%, var(--basket) 55%, #4a3124 100%);
    border-radius: 40px 60px 0 0;
  }
</style>
</head>
<body>
  <main class="coupon">
    <div class="hero-photo" role="img" aria-label="Photo of a woman resting on a pile of fresh laundry next to an iron"></div>

    <div class="washer-illustration" role="img" aria-label="Illustration of a blue front-loading washing machine"></div>

    <div class="logo">
      <span class="logo-mark"></span>
      <span class="logo-name">Suds on Fifth</span>
    </div>

    <h1 class="headline">FREE WASH-N-FOLD LAUNDRY SERVICE</h1>

    <svg class="offer-bubble" viewBox="0 0 500 330" aria-hidden="true">
      <path d="M22 0 H478 Q500 0 500 22 V250 Q500 272 478 272 H132 L76 325 L86 272 H22 Q0 272 0 250 V22 Q0 0 22 0 Z"
            fill="var(--brand-orange)" stroke="var(--brand-orange-dark)" stroke-width="2"/>
      <path d="M26 10 H474 Q490 10 490 26 V246 Q490 262 474 262 H128 L90 298 L96 262 H26 Q10 262 10 246 V26 Q10 10 26 10 Z"
            fill="none" stroke="#ffffff" stroke-width="2" stroke-dasharray="7 5" opacity="0.85"/>
    </svg>

    <svg class="care-icons" viewBox="0 0 220 36" fill="none" stroke="#ffffff" stroke-width="2" opacity="0.85" aria-hidden="true">
      <circle cx="18" cy="18" r="12"/><path d="M6 6 L30 30 M30 6 L6 30"/>
      <path d="M52 10 L56 28 H76 L80 10 M52 14 H80"/>
      <rect x="100" y="6" width="24" height="24"/><circle cx="112" cy="18" r="7"/>
      <path d="M142 28 H172 L166 12 H150 Z"/>
      <path d="M186 30 L201 6 L216 30 Z M186 8 L216 30 M216 8 L186 30"/>
    </svg>

    <div class="offer-amount">
      <span class="number">50</span>
      <span class="unit">POUNDS</span>
    </div>

    <p class="offer-terms">of laundry<br>per coupon</p>

    <p class="limit-note">(One coupon per customer)</p>
    <div class="expiry-field"></div>
    <p class="expiry-label">expiration date</p>

    <div class="basket-photo" role="img" aria-label="Photo of a wicker basket holding rolled towels"></div>

    <div class="contact">
      <p class="phone">
        <svg viewBox="0 0 24 24" aria-hidden="true"><path fill="#1c1c1c" d="M6.6 10.8a15.1 15.1 0 0 0 6.6 6.6l2.2-2.2a1 1 0 0 1 1-.25 11.4 11.4 0 0 0 3.6.57 1 1 0 0 1 1 1V20a1 1 0 0 1-1 1A17 17 0 0 1 3 4a1 1 0 0 1 1-1h3.5a1 1 0 0 1 1 1c0 1.25.2 2.45.57 3.57a1 1 0 0 1-.25 1Z"/></svg>
        (555) 014-2270
      </p>
      <p class="address">1280 S 300 W Lindon, UT 84042</p>
    </div>
  </main>
</body>
</html>
```